Texas-Based Roofing Company Looking for Creative Billboard Design

We need a billboard designed for a roofing company in the Dallas - Fort Worth area. They are a tech-forward company that uses drone technology to complete roof inspections. We would like to see a design that is out-of-the-box in terms of creativity. It can be marketed towards a hail/wind storm event, or a creative approach to helping customers think of VORTANIC when it comes to roofing needs.
Updates

Low design quality

Target Market(s)

residential homeowners

Industry/Entity Type

Roofing

Requirements
Must have
• Creative approach or play on words to elevate brand awareness.

```html
<!DOCTYPE html>
<html lang="en">
<head>
<meta charset="utf-8">
<title>Vortanic Roofing Billboard</title>
<link href="https://fonts.googleapis.com/css2?family=Open+Sans:wght@400;600&family=Lato:wght@700&display=swap" rel="stylesheet">
<style>
  :root {
    --navy: #233e82;
    --deep-blue: #1b5a9a;
    --sky: #2f9fdc;
    --sky-light: #38b0e6;
    --white: #ffffff;
    --ink: #1f1f1f;
    --gold: #e2a725;
  }
  html, body {
    margin: 0;
    padding: 0;
    width: 1200px;
    height: 459px;
    overflow: hidden;
    background: var(--white);
  }
  .billboard {
    position: relative;
    width: 1200px;
    height: 459px;
    overflow: hidden;
    background: var(--navy);
  }
  .billboard__shapes {
    position: absolute;
    inset: 0;
  }
  .photo {
    position: absolute;
    border-radius: 50%;
    box-sizing: border-box;
  }
  .photo--roofer {
    left: -47px;
    top: 36px;
    width: 280px;
    height: 280px;
    border: 10px solid var(--deep-blue);
    background: linear-gradient(160deg, #d9dde2 0%, #b9bfc6 38%, #7a4a3a 60%, #5d3428 100%);
  }
  .photo--tiles {
    left: 135px;
    top: 60px;
    width: 360px;
    height: 360px;
    border: 15px solid var(--sky);
    background: linear-gradient(135deg, #c9703f 0%, #5b6670 35%, #4b5661 55%, #cf7a45 80%, #b8663a 100%);
  }
  .brand {
    position: absolute;
    left: 564px;
    top: 246px;
    width: 534px;
    text-align: center;
  }
  .brand__name {
    margin: 0;
    font-family: "Open Sans", sans-serif;
    font-weight: 600;
    font-size: 52px;
    line-height: 1.1;
    letter-spacing: 2px;
    color: var(--ink);
    white-space: nowrap;
  }
  .brand__tagline {
    margin: 6px 0 0;
    font-family: "Open Sans", sans-serif;
    font-weight: 600;
    font-size: 17px;
    line-height: 1.2;
    letter-spacing: 3.8px;
    color: var(--gold);
    white-space: nowrap;
  }
  .services {
    position: absolute;
    right: 76px;
    top: 365px;
    margin: 0;
    font-family: "Lato", sans-serif;
    font-weight: 700;
    font-size: 24px;
    line-height: 36px;
    color: var(--white);
    text-align: right;
    white-space: nowrap;
  }
</style>
</head>
<body>
<main class="billboard">
  <svg class="billboard__shapes" width="1200" height="459" viewBox="0 0 1200 459" aria-hidden="true">
    <defs>
      <linearGradient id="arcBand" x1="0" y1="0" x2="1" y2="0">
        <stop offset="0" stop-color="#2f9fdc"/>
        <stop offset="0.55" stop-color="#1f78b8"/>
        <stop offset="1" stop-color="#1d5fa2"/>
      </linearGradient>
      <linearGradient id="sweepBand" x1="0" y1="1" x2="1" y2="0">
        <stop offset="0" stop-color="#38b0e6"/>
        <stop offset="1" stop-color="#2a8fd0"/>
      </linearGradient>
    </defs>
    <path class="corner-white" d="M0 0 H436 C300 30 150 90 0 140 Z" fill="var(--white)"/>
    <path class="arc-line" d="M420 128 C600 40 780 10 870 10 C1000 10 1120 60 1200 130 V168 C1100 90 980 30 844 32 C700 34 560 80 438 140 Z" fill="var(--white)"/>
    <path class="arc-band" d="M438 140 C560 80 700 34 844 32 C980 30 1100 90 1200 168 V244 C1100 160 980 92 838 93 C700 94 560 130 449 190 Z" fill="url(#arcBand)"/>
    <path class="panel-white" d="M449 190 C560 130 700 94 838 93 C980 92 1100 160 1200 244 V353 H449 Z" fill="var(--white)"/>
    <path class="sweep-line" d="M0 420 C80 400 170 370 250 340 L258 362 C180 390 90 420 0 442 Z" fill="var(--white)"/>
    <path class="sweep-band" d="M0 442 C90 420 180 390 258 362 L240 405 C205 422 182 440 165 459 H0 Z" fill="url(#sweepBand)"/>
  </svg>

  <div class="photo photo--roofer" role="img" aria-label="Photo of a roofer in a safety vest nailing shingles on a roof under a cloudy sky"></div>
  <div class="photo photo--tiles" role="img" aria-label="Photo of a gloved hand spray-painting clay roof tiles grey"></div>

  <div class="brand">
    <h1 class="brand__name">VORTANIC ROOFING</h1>
    <p class="brand__tagline">RAISING THE STANDARD ONE ROOF AT A TIME</p>
  </div>

  <p class="services">
    • Residential Roofing • Commercial Roofing<br>
    • Painting • Electrical and Concierge VIP Services for Realtors.
  </p>
</main>
</body>
</html>
```